Business Card Design Project

I would like to redesign our business cards and change the look and feel of our marketing material, but maintain the same basic identity of our current logo.
It is my belief that it could be much better.
You can view our website at kbozt.com

   

I was looking for a completely different look.  Something much more hip and cool looking.  You can change the colors.

I like this look and feel

 http://www.omdlawfirm.com

 But obviously don’t want to copy them exactly.

 

For the back just leave the last point.

“Keep Running Your Company, and We’ll Settle Your Claim”

I want there to be space for someone to write on.

                                                                    

                                       

I like this look and feel

 http://www.omdlawfirm.com

```html
<!DOCTYPE html>
<html lang="en">
<head>
<meta charset="utf-8">
<title>Harborline Claims Group – Business Card</title>
<link rel="stylesheet" href="https://fonts.googleapis.com/css2?family=EB+Garamond:wght@400;500&display=swap">
<style>
  :root {
    --backdrop: #dfe1e5;
    --card: #eef0f1;
    --ink: #2a2a2a;
    --accent-front: #f4a12c;
    --accent-back: #2f8fd6;
    --shadow: rgba(40, 45, 60, 0.18);
  }
  * { margin: 0; padding: 0; box-sizing: border-box; }
  html, body {
    width: 1200px;
    height: 796px;
    overflow: hidden;
    background: var(--backdrop);
    font-family: "EB Garamond", Georgia, serif;
    color: var(--ink);
  }
  .stage {
    position: relative;
    width: 1200px;
    height: 796px;
  }
  .card {
    position: absolute;
    top: 250px;
    width: 520px;
    height: 297px;
    background: var(--card);
    box-shadow: 0 6px 18px var(--shadow);
    overflow: hidden;
  }
  .card--front { left: 50px; }
  .card--back { left: 630px; }

  .band { position: absolute; }
  .card--front .band { background: var(--accent-front); }
  .card--back .band { background: var(--accent-back); }

  .company-band {
    top: 15px; left: 0; width: 263px; height: 24px;
    display: flex; align-items: center; padding-left: 8px;
    white-space: nowrap;
  }
  .company-name {
    font-size: 14px; letter-spacing: 0.2px; text-transform: uppercase;
  }
  .person-band {
    top: 39px; left: 263px; right: 0; height: 27px;
    display: flex; align-items: center; justify-content: center;
  }
  .person-name { font-size: 19px; }

  .contact-list {
    position: absolute; top: 86px; left: 263px;
    list-style: none; font-size: 15px; line-height: 25px;
  }

  .address-band {
    top: 220px; left: 0; right: 0; height: 30px;
    display: flex; align-items: center; justify-content: space-between;
    padding: 0 16px; font-size: 15px;
  }

  .stripe-left { top: 22px; left: 0; width: 263px; height: 28px; }
  .stripe-right { top: 50px; left: 263px; right: 0; height: 27px; }
  .stripe-bottom { top: 229px; left: 0; right: 0; height: 30px; }

  .tagline {
    position: absolute; top: 138px; left: 0; right: 0;
    text-align: center; font-size: 17px; white-space: nowrap;
  }
</style>
</head>
<body>
  <main class="stage">
    <section class="card card--front" aria-label="Business card front">
      <div class="band company-band"><span class="company-name">Harborline Claims Group</span></div>
      <div class="band person-band"><span class="person-name">Daniel Okafor</span></div>
      <ul class="contact-list">
        <li>office : 516-555-0142</li>
        <li>cell : 917-555-0187</li>
        <li>www.kbozt.com</li>
        <li>do@kbozt.com</li>
      </ul>
      <div class="band address-band">
        <span class="street">220 Meadow Lane</span>
        <span class="city">Fairview , Ny 11790</span>
      </div>
    </section>

    <section class="card card--back" aria-label="Business card back">
      <div class="band stripe-left"></div>
      <div class="band stripe-right"></div>
      <p class="tagline">“Keep Running Your Company, and We’ll Settle Your Claim”</p>
      <div class="band stripe-bottom"></div>
    </section>
  </main>
</body>
</html>
```